Plakate für Charity Unternehmen
Zielgruppe
Orno ist ein weltweit agierendes Charity Unternehmen.
Aufgabenstellung
Wir benötigen ein 'Plakat' Design, mit dem Zweck dieses Design als Banner, Sticker oder als Schild an unseren Projekten anzubringen. Das Schild soll in zwei verschiedenen Layouts geliefert werden.
1. Eine Art Blanko Version in der das Logo und das Motto eingearbeitet sind. Dieser Teil nimmt rund 1/3 des Plakats ein. Der Rest hat einen Freiraum auf dem wir Namen der Spender oder kooperative Charity Logos einsetzen können. Diese Version wird für Zusammenarbeit verwendet.
2. Eine zweite Version nimmt das gesamte Plakat ein, hier findet sich das Logo und das Motto welche das ganze Plakat einnehmen.
In beiden Fällen sollte die Aufteilung sauber und gut leserlich sein. Das Plakat wird in Auflösungen von bis zu 1,5m mal 1m gedruckt, sollte dementsprechend also die richtige Auflösung haben. Außerdem sollten Photoshop Datei möglichst mitgeliefert werden damit wir wenn nötig Namen und Logos einsetzen können.
Das einzuarbeitende Motto lautet:
إنما المؤمنون أخوة
Das Plakat sollte im Querformat sein und die Hintergrundfarbe sollte schwarz oder weiß sein.
Anbei befindet sich eine Beispieldatei wie das Plakat an den Projekten angebracht wird.

```html
<!DOCTYPE html>
<html lang="de">
<head>
<meta charset="utf-8">
<title>Plakat Blanko – Motto und Freiraum</title>
<link rel="stylesheet" href="https://fonts.googleapis.com/css2?family=Noto+Sans+Arabic:wght@400&family=Noto+Sans:wght@400&display=swap">
<style>
  :root {
    --paper: #ffffff;
    --ink: #111111;
    --gold: #d1ae66;
    --blue: #1a75bb;
    --red: #c94a24;
  }
  html, body {
    margin: 0;
    padding: 0;
    overflow: hidden;
    background: var(--paper);
  }
  .poster {
    position: relative;
    width: 1200px;
    height: 848px;
    background: var(--paper);
    overflow: hidden;
  }
  .motto {
    position: absolute;
    top: 28px;
    right: 438px;
    margin: 0;
    direction: rtl;
    font-family: "Noto Sans Arabic", sans-serif;
    font-weight: 400;
    font-size: 100px;
    line-height: 1.4;
    color: var(--ink);
    white-space: nowrap;
  }
  .band {
    position: absolute;
    left: 0;
  }
  .band--gold-top { top: 205px; width: 793px; height: 61px; background: var(--gold); }
  .band--gold-top-end { top: 205px; left: 1104px; width: 96px; height: 61px; background: var(--gold); }
  .band--blue-top { top: 275px; width: 1200px; height: 8px; background: var(--blue); }
  .band--red-top { top: 283px; width: 1200px; height: 17px; background: var(--red); }
  .band--red-bottom { top: 746px; width: 1200px; height: 17px; background: var(--red); }
  .band--blue-bottom { top: 763px; width: 1200px; height: 8px; background: var(--blue); }
  .band--gold-bottom { top: 781px; width: 1200px; height: 67px; background: var(--gold); }

  .brand {
    position: absolute;
    left: 810px;
    top: 36px;
    width: 290px;
    height: 226px;
    display: flex;
    flex-direction: column;
    align-items: center;
    justify-content: flex-end;
  }
  .brand__mark {
    width: 140px;
    height: 140px;
    border-radius: 50%;
    background: var(--gold);
    margin-bottom: 24px;
  }
  .brand__name {
    font-family: "Noto Sans", sans-serif;
    font-weight: 400;
    font-size: 42px;
    letter-spacing: 1px;
    line-height: 1;
    color: var(--ink);
    margin-bottom: 10px;
  }
  .donor-space {
    position: absolute;
    top: 300px;
    left: 0;
    width: 1200px;
    height: 446px;
  }
</style>
</head>
<body>
  <main class="poster">
    <h1 class="motto">إنما المؤمنون أخوة</h1>

    <div class="band band--gold-top"></div>
    <div class="band band--gold-top-end"></div>
    <div class="band band--blue-top"></div>
    <div class="band band--red-top"></div>

    <div class="brand">
      <div class="brand__mark"></div>
      <div class="brand__name">VELDRAN</div>
    </div>

    <section class="donor-space" aria-label="Freiraum für Spender und Partner"></section>

    <div class="band band--red-bottom"></div>
    <div class="band band--blue-bottom"></div>
    <div class="band band--gold-bottom"></div>
  </main>
</body>
</html>
```